Brightpath Holdings Business Card

Create a two sided, high gloss, quality business card for Brightpath Holdings.

Target Market(s)

People wanting to purchase, scale, and sell businesses.

Industry/Entity Type

Entrepreneurs

Contact Information for Business Card

One line: Dana Corwell, CPA, CMA Another line: Entrepreneur & Investor Another line: Business Ownership Transition Expert Another line: Multi-State Licensed Real Estate Broker Phone 954-BRTPATH (278-7284) Email Dana@Brightpath Holdings.com Website www.Brightpath.com

Requirements
Must have
• Black Card, logo on one side, all other information on the other side including a small logo.
Nice to have
• Possibly add a tagline "Helping entrepreneurs live a life they don't need a vacation from"
Should not have
• There will not be a mailing address on these cards.

```html
<!DOCTYPE html>
<html lang="en">
<head>
<meta charset="utf-8">
<title>Brightpath Holdings – Business Card</title>
<link href="https://fonts.googleapis.com/css2?family=Montserrat:wght@400;600;700&display=swap" rel="stylesheet">
<style>
  :root {
    --page-bg: #f1f1f1;
    --card-black: #060708;
    --gold: #d8b048;
    --gold-light: #f3d97a;
    --gold-deep: #b8862a;
    --text-white: #f2f2f2;
  }
  * { margin: 0; padding: 0; box-sizing: border-box; }
  html, body { width: 1200px; height: 1200px; overflow: hidden; }
  body {
    background: var(--page-bg);
    font-family: "Montserrat", Arial, sans-serif;
    position: relative;
  }
  .card {
    position: absolute;
    left: 166px;
    width: 865px;
    height: 519px;
    background: var(--card-black);
    box-shadow: 0 2px 6px rgba(0,0,0,0.18);
    overflow: hidden;
  }
  .card--front { top: 71px; }
  .card--back { top: 634px; }

  .brand {
    position: absolute;
    display: flex;
    align-items: center;
    gap: 14px;
    color: var(--gold);
    font-weight: 700;
    white-space: nowrap;
  }
  .brand__dot {
    border-radius: 50%;
    background: var(--gold);
    flex: none;
  }
  .card--front .brand { left: 52px; top: 110px; font-size: 34px; }
  .card--front .brand__dot { width: 22px; height: 22px; }
  .card--back .brand { left: 92px; top: 300px; font-size: 50px; gap: 18px; }
  .card--back .brand__dot { width: 30px; height: 30px; }

  .holder {
    position: absolute;
    left: 52px;
    top: 234px;
  }
  .holder__name {
    font-size: 32px;
    font-weight: 700;
    color: var(--gold-light);
    letter-spacing: 0.5px;
    margin-bottom: 10px;
  }
  .holder__credentials { color: var(--gold); }
  .holder__role {
    font-size: 19.5px;
    font-weight: 400;
    color: var(--text-white);
    line-height: 27px;
    letter-spacing: 0.3px;
  }

  .accent-line {
    position: absolute;
    left: 0; top: 0;
    width: 865px; height: 519px;
  }

  .contact {
    position: absolute;
    right: 52px;
    top: 386px;
    list-style: none;
    text-align: right;
  }
  .contact__item {
    font-size: 18.5px;
    color: var(--text-white);
    line-height: 27px;
    display: flex;
    justify-content: flex-end;
    align-items: center;
    gap: 12px;
    letter-spacing: 0.3px;
  }
  .contact__icon { width: 11px; height: 11px; fill: var(--text-white); flex: none; }

  .star-area {
    position: absolute;
    background: radial-gradient(circle, rgba(243,217,122,0.85) 0%, rgba(184,134,42,0.35) 45%, rgba(6,7,8,0) 72%);
  }
  .star-area--large { left: 711px; top: 99px; width: 100px; height: 100px; }
  .star-area--small { left: 676px; top: 87px; width: 24px; height: 24px; }

  .corner-glow {
    position: absolute;
    left: 534px;
    top: 0;
    width: 331px;
    height: 320px;
    background: radial-gradient(ellipse at 100% 0%, rgba(243,217,122,0.55) 0%, rgba(184,134,42,0.25) 45%, rgba(6,7,8,0) 75%);
  }
</style>
</head>
<body>

  <section class="card card--front" aria-label="Business card front">
    <div class="brand">
      <span class="brand__dot"></span>
      <span class="brand__name">Brightpath Holdings</span>
    </div>

    <div class="star-area star-area--small" role="img" aria-label="Small gold compass star ornament"></div>
    <div class="star-area star-area--large" role="img" aria-label="Gold compass star ornament"></div>

    <svg class="accent-line" viewBox="0 0 865 519" aria-hidden="true">
      <defs>
        <linearGradient id="streak" x1="0" y1="1" x2="1" y2="0">
          <stop offset="0" stop-color="#b8862a" stop-opacity="0.3"/>
          <stop offset="0.5" stop-color="#f3d97a"/>
          <stop offset="1" stop-color="#b8862a" stop-opacity="0.2"/>
        </linearGradient>
      </defs>
      <polygon points="296,448 696,290 697,292 298,449" fill="url(#streak)"/>
    </svg>

    <div class="holder">
      <h1 class="holder__name">Dana Corwell, <span class="holder__credentials">CPA, CMA</span></h1>
      <p class="holder__role">Entrepreneur &amp; Investor</p>
      <p class="holder__role">Business Ownership Transition Expert</p>
      <p class="holder__role">Multi-State Licensed Real Estate Broker</p>
    </div>

    <ul class="contact">
      <li class="contact__item">954-BRTPATH (278-7284)
        <svg class="contact__icon" viewBox="0 0 12 12" aria-hidden="true"><path d="M2.5 1 L4.5 3.5 L3.5 4.8 Q4.8 7.2 7.2 8.5 L8.5 7.5 L11 9.5 L10 11 Q5 11 1 2 Z"/></svg>
      </li>
      <li class="contact__item">Dana@Brightpath Holdings.com
        <svg class="contact__icon" viewBox="0 0 12 12" aria-hidden="true"><path d="M1 2.5 H11 V9.5 H1 Z M1.5 3 L6 6.5 L10.5 3" stroke="#060708" stroke-width="0.8"/></svg>
      </li>
      <li class="contact__item">www.Brightpath.com
        <svg class="contact__icon" viewBox="0 0 12 12" aria-hidden="true"><circle cx="6" cy="6" r="5"/><path d="M1 6 H11 M6 1 Q3 6 6 11 Q9 6 6 1" stroke="#060708" stroke-width="0.8" fill="none"/></svg>
      </li>
    </ul>
  </section>

  <section class="card card--back" aria-label="Business card back">
    <div class="corner-glow" role="img" aria-label="Large gold brand decoration in the top right corner"></div>
    <div class="brand">
      <span class="brand__dot"></span>
      <span class="brand__name">Brightpath Holdings</span>
    </div>
  </section>

</body>
</html>
```